KORVELTA Corporate Business Card

Modern business card design for company which focuses in the areas of Staffing, IT Consulting & Data Services. Please note: We are no longer using the IT subscript on the logo. All designs should have IT subscript removed.
Website: www.korveltait.example

```html
<!DOCTYPE html>
<html lang="en">
<head>
<meta charset="UTF-8">
<title>KORVELTA Business Card</title>
<link href="https://fonts.googleapis.com/css2?family=Lato:wght@400;700&display=swap" rel="stylesheet">
<style>
  :root {
    --backdrop: #3a3a3d;
    --card: #17171c;
    --accent: #2a9ee0;
    --text-light: #d9d9dc;
    --divider: #55555c;
  }
  * { box-sizing: border-box; margin: 0; padding: 0; }
  html, body { width: 1200px; height: 1015px; overflow: hidden; }
  body {
    background: var(--backdrop);
    font-family: "Lato", sans-serif;
    display: flex;
    flex-direction: column;
    align-items: center;
    justify-content: center;
    gap: 56px;
  }
  .card {
    position: relative;
    width: 700px;
    height: 400px;
    background: var(--card);
    box-shadow: 0 12px 28px rgba(0,0,0,0.45);
    overflow: hidden;
  }
  .card__band {
    position: absolute;
    left: 0; right: 0; bottom: 0;
    height: 14px;
    background: var(--accent);
  }
  .brand {
    display: flex;
    align-items: center;
    gap: 14px;
    color: var(--accent);
    font-weight: 700;
    letter-spacing: 3px;
  }
  .brand__mark {
    width: 40px; height: 40px;
    background: var(--accent);
  }
  .card--front .brand {
    position: absolute;
    left: 50%; top: 50%;
    transform: translate(-50%, -60%);
    font-size: 62px;
  }
  .card--front .brand__mark { width: 50px; height: 50px; }
  .card--back .brand {
    position: absolute;
    left: 44px; top: 50%;
    transform: translateY(-50%);
    font-size: 44px;
  }
  .card--back .brand__mark { width: 34px; height: 34px; }
  .divider {
    position: absolute;
    left: 385px; top: 80px;
    width: 1px; height: 220px;
    background: var(--divider);
  }
  .contact {
    position: absolute;
    left: 410px; top: 86px;
    color: var(--text-light);
    font-size: 15px;
    line-height: 1.45;
  }
  .contact__name {
    color: var(--accent);
    font-size: 20px;
    font-weight: 400;
    letter-spacing: 0.5px;
  }
  .contact__role { font-size: 16px; margin-bottom: 12px; }
  .contact__row { display: flex; align-items: center; gap: 8px; }
  .contact__row svg { width: 13px; height: 13px; fill: var(--accent); flex: none; }
  .contact__address { margin-top: 14px; }
</style>
</head>
<body>
  <section class="card card--front">
    <div class="brand"><span class="brand__mark"></span>KORVELTA</div>
    <div class="card__band"></div>
  </section>

  <section class="card card--back">
    <div class="brand"><span class="brand__mark"></span>KORVELTA</div>
    <div class="divider"></div>
    <div class="contact">
      <div class="contact__name">DANIEL MARSH</div>
      <div class="contact__role">Managing Director</div>
      <div class="contact__row">
        <svg viewBox="0 0 16 16"><path d="M3 1h3l1.5 4-2 1.3a9 9 0 0 0 4.2 4.2L11 8.5l4 1.5v3a2 2 0 0 1-2 2C6.9 15 1 9.1 1 3a2 2 0 0 1 2-2z"/></svg>
        555-014-2290
      </div>
      <div class="contact__row">
        <svg viewBox="0 0 16 16"><path d="M1 3h14v10H1z M1 3l7 6 7-6" stroke="#17171c" stroke-width="1.2"/></svg>
        contactus@korveltait.example
      </div>
      <div class="contact__row">
        <svg viewBox="0 0 16 16"><circle cx="8" cy="8" r="7"/></svg>
        www.korveltait.example
      </div>
      <div class="contact__address">418 Alder Street<br>Brookfield, IN 40010</div>
    </div>
    <div class="card__band"></div>
  </section>
</body>
</html>
```